We are a printed circuit board manufacturer. Need a company professional web site to allow our potential customers to know more about our background, capability and our products. The web site will contain three languages, which are Chinese, English and Japanese. Our audience are mainly electronic companies that procure printed circuit boards. I have a word document that have all the required text in all three languages. The final design should communicate the impression that we embrace quality, trustworthiness and long term partnership business principles.
We should have sections that allow us to post pictures of our facilities.
I have added the three files in three different languages.
Some of the information is below:
Background
RVT Harbourline Limited (RVT) was set up in Hong Kong in 2007 by two Hong Kong entrepreneurs, Mr. Dao Lanh and Mr. Tai Pak. We acquired the single sided printed circuit board factory located in Dongguan City, Guangdong Province, China, from Tolvane Corporation of the U.S. in 2007. In addition to RVT, Mr. Lanh and Mr. Pak also own Brightwell Technology Company Limited, a semiconductor company based in Hong Kong since 1997 with a total investment of over US$100 million. Brightwell is engaged in the manufacturing of flexible substrates and MEMS assembly business.
RVT has been awarded TS 16949 and ISO14000 certificates since 2009 and 2004 respectively.
Business Principles
RVT Harbourline Limited strives to be a professional top notched printed circuit board supplier. We embrace four “EXCELLENCE” principles, namely, excellence in quality, excellence in prices, excellence in services and excellence in on time delivery.
We approach each customer with a long-term partnership view that delivers the lowest ownership costs and highest total values to our customers. We customize quotations and solutions in order to allow our customers to win more businesses. We believe by thinking from our customers’ points of view we will be able to create a WIN-WIN relationship.
Customers
Due to our excellent quality, services and production systems, RVT Harbourline Limited manage to service a number of large Japanese and US customers, which include:
Technical capability overview
Below is an overview of our current capability:
Target Market(s)
Electronic companies buyers
Industry/Entity Type
Business
Requirements
Must have
- Capability description
Should not have
- no cartoon

```html
<!DOCTYPE html>
<html lang="en">
<head>
<meta charset="utf-8">
<title>RVT Harbourline Limited</title>
<link href="https://fonts.googleapis.com/css2?family=Arimo:wght@400;700&family=Didact+Gothic&family=Noto+Serif+SC:wght@700&display=swap" rel="stylesheet">
<style>
:root{
  --page:#e4e3dd;
  --header:#f4f4f1;
  --panel:#ffffff;
  --tab:#e6e5df;
  --navy:#2b4052;
  --btn:#2f5478;
  --green:#1f6b45;
  --text:#333333;
  --muted:#888888;
  --tan:#a6976a;
  --black:#111111;
}
*{box-sizing:border-box;margin:0;padding:0}
html,body{width:945px;height:1200px;overflow:hidden}
body{background:var(--page);font-family:"Arimo",Arial,sans-serif;color:var(--text);position:relative}
a{color:inherit;text-decoration:none}
.abs{position:absolute}
.site-header{left:0;top:0;width:945px;height:57px;background:var(--header)}
.brand{left:104px;top:7px;width:179px;height:48px;background:#fff;display:flex;flex-direction:column;align-items:center;justify-content:center;color:var(--green);font-family:"Didact Gothic",sans-serif;font-size:17px;line-height:18px;text-align:center}
.account{right:106px;top:16px;font-size:8px;color:var(--text)}
.account span{margin:0 6px}
.search{left:673px;top:31px;width:169px;height:17px;background:#e3e2dc;border:1px solid #c9c8c2}
.search svg{position:absolute;right:3px;top:2px}
.nav{left:104px;top:70px;width:738px;height:31px;background:#f4f4f1;display:flex;align-items:center;font-size:12px;color:#222}
.nav a{margin-right:21px}
.nav .current{background:var(--navy);color:#fff;height:28px;width:80px;display:flex;align-items:center;justify-content:center;margin:0 23px 0 21px;border-bottom:3px solid #cfd4d8}
.lang{right:12px;top:8px;width:117px;height:14px;border:1px solid #999;font-size:8px;padding:2px 4px;position:absolute;background:#f7f7f5}
.lang i{position:absolute;right:0;top:0;width:24px;height:12px;border-left:1px solid #999}
.lang i:after{content:"";position:absolute;left:7px;top:4px;border:5px solid transparent;border-top:5px solid #333;border-bottom:0}
.slider{left:104px;top:123px;width:739px;height:264px;background:#fff;border:1px solid #999;padding:3px}
.slide{width:100%;height:100%;background:radial-gradient(ellipse at 45% 35%,#5fa0b8 0%,#1d4a5a 35%,#0c1c22 75%,#070d10 100%);position:relative}
.slide h2{position:absolute;right:18px;bottom:12px;color:#fff;font-weight:700;font-size:17px;line-height:23px;text-align:right;letter-spacing:.8px}
.arrow{position:absolute;top:121px;width:24px;height:24px;border-radius:50%;background:#fff}
.pager{left:763px;top:118px;width:73px;height:20px;background:#fff;border:1px solid #aaa;display:flex;gap:4px;align-items:center;justify-content:center}
.pager b{width:9px;height:7px;background:#999}
.content-band{left:104px;top:427px;width:738px;height:507px;background:#efeeea}
.box{background:var(--panel);border-top:5px solid #e9e8e3;box-shadow:0 0 1px #bbb}
.tab{display:inline-block;background:var(--tab);font-size:10.5px;padding:5px 10px 3px;margin:0 0 0 6px;color:var(--text);letter-spacing:.3px}
.testimonial{left:124px;top:409px;width:188px;height:126px}
.quote{left:11px;top:38px;width:170px;font-size:7.5px;line-height:12.3px;color:var(--text)}
.avatar{float:left;width:33px;height:31px;margin:2px 23px 0 3px;background:linear-gradient(#9aa3ab,#4c5560)}
.viewall{right:17px;bottom:11px;font-family:"Didact Gothic",serif;font-size:10px;text-decoration:underline;color:var(--text)}
.clients{left:124px;top:554px;width:188px;height:210px}
.client-list{left:-6px;top:40px;width:188px}
.client{position:relative;background:#e8e7e1;height:25px;margin-bottom:9px;font-size:10px;font-weight:700;color:#2a2a2a;padding:0 0 0 18px;display:flex;align-items:center;line-height:11px;width:188px}
.client.active{background:#f4f4f1;border:1px solid #666;box-shadow:0 1px 2px #888}
.client .car{position:absolute;right:12px;top:10px;border:6px solid transparent;border-top:6px solid #555;border-bottom:0}
.client.active .car{top:7px;right:14px;border:5px solid transparent;border-left:7px solid #555;border-right:0}
.contact{left:124px;top:783px;width:188px;height:145px}
.contact h4{left:12px;top:46px;font-size:10px;font-weight:400;text-decoration:underline;color:var(--navy)}
.contact p{left:12px;top:70px;font-size:9.6px;line-height:11px;letter-spacing:.5px;color:var(--text)}
.welcome{left:336px;top:440px;width:490px}
.welcome h1{font-family:"Didact Gothic",sans-serif;font-weight:400;font-size:18px;color:#222;margin-bottom:7px}
.welcome p{font-size:7.6px;line-height:12.3px;color:var(--text);letter-spacing:.2px}
.btn{display:inline-block;background:var(--btn);color:#fff;font-size:9px;padding:3px 10px;border-bottom:2px solid #1c3550}
.customers{left:330px;top:556px;width:491px;height:209px}
.customers h3{left:21px;top:19px;font-size:10px;font-weight:700;text-decoration:underline;color:#222}
.customers .lead{left:21px;top:45px;width:460px;font-size:8.6px;line-height:14px;color:var(--muted);letter-spacing:.3px}
.cn-title{left:165px;top:97px;font-family:"Noto Serif SC",serif;font-size:26px;color:var(--green)}
.partners{left:21px;top:128px;width:462px;height:56px;border-bottom:1px solid #ccc}
.partner-cat{left:18px;top:17px;font-size:11px;font-weight:700;color:var(--text);line-height:13px;text-align:center}
.partner-div{left:76px;top:0;width:1px;height:50px;background:#bbb}
.mark{font-family:"Arimo",sans-serif;font-weight:400;font-size:12px;color:var(--text);letter-spacing:.3px}
.recent{left:335px;top:780px;width:490px}
.recent h3{font-family:"Didact Gothic",sans-serif;font-weight:400;font-size:12px;color:#222;letter-spacing:.5px}
.work{top:21px;width:116px}
.thumb{width:116px;height:49px;border:1px solid #7a8aa0;background:#fff;display:flex;align-items:center;justify-content:center}
.thumb i{display:block;width:84px;height:30px;border-radius:3px}
.work p{font-size:7.5px;line-height:9px;color:var(--text);margin-top:9px}
.work a{display:block;font-size:7.5px;color:var(--text);margin-top:7px}
.order{left:104px;top:941px;width:738px;height:56px;background:#f2f1ed;border-top:5px solid #e9e8e3}
.order h4{left:17px;top:8px;font-size:10.5px;font-weight:400;text-decoration:underline;color:var(--navy);letter-spacing:.5px}
.order label{font-size:9px;color:#444;top:37px}
.field{top:26px;width:152px;height:18px;background:#e4e3dd;border:1px solid #c5c4be}
.send{left:638px;top:28px;width:76px;height:16px;background:var(--btn);color:#fff;font-size:9.5px;text-align:center;line-height:16px}
.footer{left:104px;top:1012px;width:738px;height:162px;background:var(--navy)}
.footer h5{font-size:12px;font-weight:400;color:#fff;letter-spacing:.3px}
.footer p,.footer li{font-size:8.6px;line-height:10.3px;color:var(--tan);letter-spacing:.3px}
.footer ul{list-style:none}
.footer li{margin-bottom:7.5px;padding-left:18px;position:relative}
.footer li:before{content:">";position:absolute;left:0;color:#ddd}
.tweet{padding-left:20px;position:relative;margin-bottom:12px}
.tweet b{position:absolute;left:0;top:1px;width:11px;height:9px;background:#cfd6dc;border-radius:50% 50% 50% 10%}
.social{display:flex;gap:8px;margin-top:12px}
.social i{width:17px;height:17px;border-radius:50%;background:#b8c0c6}
.news-field{width:166px;height:20px;background:#eeeeea;border:1px solid #bbb;margin-top:13px}
.join{display:inline-block;margin-top:16px;background:var(--black);color:#fff;font-size:10px;padding:4px 9px}
.bottom{left:104px;top:1174px;width:738px;height:26px;background:var(--black);color:#fff;font-size:8.6px;display:flex;justify-content:space-between;align-items:center;padding:0 21px}
</style>
</head>
<body>
<header class="site-header abs">
  <div class="brand abs">RVT<br>Harbourline Limited</div>
  <div class="account abs">My Account<span>|</span>Log in</div>
  <div class="search abs"><svg width="13" height="13" viewBox="0 0 13 13"><circle cx="5" cy="5" r="3.8" fill="none" stroke="#222" stroke-width="1.6"/><line x1="8" y1="8" x2="12" y2="12" stroke="#222" stroke-width="2"/></svg></div>
</header>

<nav class="nav abs">
  <a class="current">Home</a>
  <a>Services</a><a>Capabilities</a><a>Testimonial</a><a>News</a><a>Our clients</a><a>Contacts Us</a>
  <div class="lang">Select Language<i></i></div>
</nav>

<section class="slider abs">
  <div class="slide" role="img" aria-label="Close-up of a circuit board with microchips under blue light">
    <div class="arrow" style="left:10px"><svg width="24" height="24"><path d="M14 7l-5 5 5 5" fill="none" stroke="#222" stroke-width="2.4"/></svg></div>
    <div class="arrow" style="right:10px"><svg width="24" height="24"><path d="M10 7l5 5-5 5" fill="none" stroke="#222" stroke-width="2.4"/></svg></div>
    <h2>THE PREMIER INDUSTRIAL<br>MANUFACTUER AND EXPORTER.</h2>
  </div>
</section>
<div class="pager abs"><b></b><b></b><b></b><b></b></div>

<div class="content-band abs"></div>

<aside class="testimonial box abs">
  <span class="tab">TESTIMONIAL</span>
  <p class="quote abs"><span class="avatar" role="img" aria-label="Portrait of a client representative"></span>Lorem ipsum dolor sit amet, consectetur adipiscing elit. Nullam mattis lorem quis enim tristique luctus. In hac habitasse platea dictumst.</p>
  <a class="viewall abs">View All</a>
</aside>

<aside class="clients box abs">
  <span class="tab">OUR CLIENTS</span>
  <div class="client-list abs">
    <div class="client active">AUTO Motive<span class="car"></span></div>
    <div class="client">Video &amp; Audio<span class="car"></span></div>
    <div class="client">Home Appliances<br>&amp; Camera<span class="car"></span></div>
    <div class="client">Industrial Equipmen &amp;<br>Power Supplier<span class="car"></span></div>
    <div class="client">Contract Manufacturers<span class="car"></span></div>
  </div>
</aside>

<aside class="contact box abs">
  <span class="tab">CONTACT US</span>
  <h4 class="abs">Hong Kong Business Office</h4>
  <p class="abs">28/F Quayside Tower<br>12 Marlow Road<br>North Point, HONG KONG<br>Telephone: (852)30000123<br>Fax: (852)30000456<br>Email: sales@rvtboard.example</p>
</aside>

<section class="welcome abs">
  <h1>Welcome To RVT Harbourline Limited !</h1>
  <p><b>RVT Harbourline Limited</b> (RVT) was set up in Hong Kong in 2007 by two Hong Kong entrepreneurs, Mr. Dao Lanh and Mr. Tai Pak. We acquired the single sided printed circuit board factory located in Dongguan City, Guangdong Province, China, from Tolvane Corporation of the U.S. in 2007. In addition to RVT, Mr. Lanh and Mr. Pak also own Brightwell Technology Company Limited, a semiconductor company based in Hong Kong since 1997 with a total investment of over US$100 million.</p>
  <span class="btn" style="margin-top:4px">Learn More</span>
</section>

<section class="customers box abs">
  <h3 class="abs">Customers</h3>
  <p class="lead abs">Due to our excellent quality, services and production systems, RVT Harbourline Limited manage to service a number of large Japanese and US customers, which include:</p>
  <div class="cn-title abs">主要客户群</div>
  <div class="partners abs">
    <div class="partner-cat abs">Auto<br>Motive</div>
    <div class="partner-div abs"></div>
    <div class="mark abs" style="left:140px;top:10px">Harrowgate Systems</div>
    <div class="mark abs" style="left:130px;top:34px">Keldor</div>
    <div class="mark abs" style="left:230px;top:34px">Okaru Drive</div>
    <div class="mark abs" style="left:380px;top:16px">Lumera</div>
  </div>
</section>

<section class="recent abs">
  <h3>RECNT WORK</h3>
  <div class="work abs" style="left:0">
    <div class="thumb"><i role="img" aria-label="Green printed circuit board" style="background:linear-gradient(#4f7a3c,#2d4e2a)"></i></div>
    <p>Lorem ipsum dolor sit amet, consect etur adipiscing elit.</p><a>Read More...</a>
  </div>
  <div class="work abs" style="left:175px">
    <div class="thumb"><i role="img" aria-label="Flexible orange circuit board" style="background:linear-gradient(#d07a2a,#8a3f12);height:14px"></i></div>
    <p>Lorem ipsum dolor sit amet, consect etur adipiscing elit.</p><a>Read More...</a>
  </div>
  <div class="work abs" style="left:351px">
    <div class="thumb"><i role="img" aria-label="Assembled circuit board with components" style="background:linear-gradient(#7f9a6a,#3d5a3a)"></i></div>
    <p>Lorem ipsum dolor sit amet, consect etur adipiscing elit.</p><a>Read More...</a>
  </div>
</section>

<section class="order abs">
  <h4 class="abs">ODERS NOW</h4>
  <label class="abs" style="left:17px">Name</label><div class="field abs" style="left:50px"></div>
  <label class="abs" style="left:221px">Aderss</label><div class="field abs" style="left:260px"></div>
  <label class="abs" style="left:430px">Phone</label><div class="field abs" style="left:466px"></div>
  <div class="send abs">Send Now</div>
</section>

<footer class="footer abs">
  <div class="abs" style="left:21px;top:14px;width:160px">
    <h5>About Us</h5>
    <p style="margin-top:12px">Sed ut perspiciatis unde omnis iste natus error sit voluptatem accusa-ntium doloremque laudantium, totam rem aperiam.</p>
    <h5 style="margin-top:20px">Find Us Elsewhere</h5>
    <div class="social"><i></i><i></i><i></i><i></i><i></i></div>
  </div>
  <div class="abs" style="left:201px;top:14px;width:170px">
    <h5>From Pulse</h5>
    <div style="margin-top:12px">
      <p class="tweet"><b></b>about 2 days ago @rvtnews<br>@rvt feed.example.com</p>
      <p class="tweet"><b></b>about 2 days ago @rvtnews<br>@rvt feed.example.com</p>
      <p class="tweet"><b></b>about 2 days ago @rvtnews<br>@rvt feed.example.com</p>
    </div>
  </div>
  <div class="abs" style="left:385px;top:14px;width:160px">
    <h5>Categories</h5>
    <ul style="margin-top:12px">
      <li>Lorem ipsum dolor sit amet,</li>
      <li>Aliquam lorem ante.</li>
      <li>Consequat vitae.</li>
      <li>Leo eget bibendum sodales.</li>
      <li>Donec sodales sagittis mag. Sed consequat.</li>
    </ul>
  </div>
  <div class="abs" style="left:552px;top:14px;width:170px">
    <h5>Join Our Newsletter</h5>
    <p style="margin-top:12px">Nam quam nunc, blandit vel, luctus pulvinar, hendrerit id, lorem. Maece nec odio et ante tincidunt.</p>
    <div class="news-field"></div>
    <span class="join">Join Now</span>
  </div>
</footer>
<div class="bottom abs"><span>Site Map | Search Tems | Advanced | Orders and Returns | Contact Us</span><span>© 2012 | Privacy policy</span></div>
</body>
</html>
```